BEXOR (non-profit) advertisement for 5K Walk for awareness and stigma removal

I am a Support group facilitator for BEXOR, Bright Extended Outreach Resource.
BEXOR National will be holding a 5K run in Virginia...They are encouraging us support group facilitators to hold local events on the same day, May 18, 2014.
I am holding a walk in Hollins Park in Medford, NJ...having people sign up as a virtual walker with a link provided as well as emailing me to confirm themselves as a walker at my event.
I would love to use the BEXOR Logo on this flyer and market away!
The bexor logo is on my website, www.plumvoicehub.example

Industry/Entity Type

Events

Requirements
Nice to have
• BEXOR LOGO
a pic of walkers, runners/families

```html
<!DOCTYPE html>
<html lang="en">
<head>
<meta charset="utf-8">
<title>BEXOR 5K Walk for Awareness and Stigma Removal</title>
<link rel="stylesheet" href="https://fonts.googleapis.com/css2?family=Permanent+Marker&family=Arimo:wght@700&family=Noto+Serif:ital,wght@1,700&display=swap">
<style>
  :root {
    --park-green: #5e7a46;
    --park-dark: #2f4127;
    --sky: #c9d6c2;
    --ribbon-red: #e3262a;
    --ribbon-blue: #2c3a92;
    --ribbon-yellow: #f7e11b;
    --logo-blue: #2e3a94;
    --date-red: #e8241f;
    --panel-red: #e6302a;
    --panel-light: #f07a47;
    --ink: #111111;
    --white: #ffffff;
  }
  * { box-sizing: border-box; margin: 0; padding: 0; }
  html, body { width: 1200px; height: 900px; overflow: hidden; background: #fff; }
  .flyer { position: relative; width: 1200px; height: 900px; overflow: hidden; }
  .scene { position: absolute; inset: 0; }
  .scene-park {
    background: linear-gradient(160deg, #8e9a7c 0%, var(--park-green) 30%, var(--park-dark) 55%, #7d8e5a 80%, #b9c08c 100%);
  }
  .scene-families {
    clip-path: polygon(0 400px, 330px 430px, 470px 900px, 0 900px);
    background: linear-gradient(180deg, #6f8d4f 0%, #b8a48c 45%, #a3b27a 100%);
  }
  .scene-runners {
    clip-path: polygon(300px 300px, 560px 272px, 820px 390px, 1200px 560px, 1200px 900px, 470px 900px, 330px 430px);
    background: linear-gradient(150deg, #a86a3a 0%, #c89b6b 20%, #6c6f72 45%, #3d3f44 75%, #7b7672 100%);
  }
  .scene-faded {
    clip-path: polygon(560px 272px, 1200px 300px, 1200px 560px, 820px 390px);
    background: linear-gradient(180deg, #f3f0ea 0%, #e6e2d8 100%);
    opacity: .92;
  }
  .scene-faded-lower {
    clip-path: polygon(900px 420px, 1200px 560px, 1200px 900px, 1000px 900px);
    background: linear-gradient(180deg, rgba(255,255,255,.65), rgba(255,255,255,.25));
  }
  .ribbons { position: absolute; inset: 0; }
  .footprints {
    position: absolute; left: 372px; top: 18px; width: 190px; height: 200px;
    background: radial-gradient(ellipse at center, rgba(255,255,255,.5), rgba(255,255,255,0) 70%);
  }
  .logo-badge {
    position: absolute; left: 68px; top: 215px; width: 264px; height: 264px;
    border-radius: 50%; background: var(--white);
    display: flex; align-items: center; justify-content: center;
  }
  .logo-name {
    font-family: "Arimo", sans-serif; font-weight: 700; font-size: 52px;
    color: var(--logo-blue); letter-spacing: 1px;
  }
  .title {
    position: absolute; left: 550px; top: 22px; width: 620px; text-align: center;
    font-family: "Permanent Marker", cursive; color: var(--white);
    text-shadow: 3px 3px 0 var(--ink), -2px -2px 0 var(--ink), 2px -2px 0 var(--ink), -2px 2px 0 var(--ink);
    line-height: 1;
  }
  .title-main { display: block; font-size: 112px; }
  .title-sub { display: block; font-size: 50px; margin-top: 16px; }
  .title-sub + .title-sub { margin-top: 18px; }
  .extras {
    position: absolute; left: 672px; top: 304px; width: 500px;
    font-family: "Noto Serif", serif; font-style: italic; font-weight: 700;
    font-size: 22px; line-height: 1.45; color: var(--white);
    text-shadow: 2px 2px 0 var(--ink), -1px -1px 0 var(--ink), 1px -1px 0 var(--ink), -1px 1px 0 var(--ink);
  }
  .event-details {
    position: absolute; left: 780px; top: 418px; width: 380px; text-align: center;
    font-family: "Permanent Marker", cursive; color: var(--date-red);
    text-shadow: 2px 2px 0 var(--ink), -2px -2px 0 var(--ink), 2px -2px 0 var(--ink), -2px 2px 0 var(--ink);
    line-height: 1.05;
  }
  .event-date { display: block; font-size: 46px; }
  .event-time { display: block; font-size: 40px; }
  .event-place { display: block; font-size: 34px; margin-top: 2px; }
  .signup-panel {
    position: absolute; left: 0; top: 718px; width: 720px; height: 182px;
    clip-path: polygon(0 0, 720px 0, 565px 182px, 0 182px);
    background: linear-gradient(90deg, var(--panel-red) 0%, var(--panel-red) 55%, var(--panel-light) 100%);
  }
  .signup-text {
    position: absolute; left: 0; top: 722px; width: 640px; text-align: center;
    font-family: "Arimo", sans-serif; font-weight: 700; color: var(--ink);
    line-height: 1.2;
  }
  .signup-heading { display: block; font-size: 23px; }
  .signup-link { display: block; font-size: 15px; margin-top: 4px; line-height: 1.5; }
  .signup-or { display: block; font-size: 26px; margin-top: 2px; }
  .signup-email { display: block; font-size: 25px; }
  .signup-confirm { display: block; font-size: 21px; margin-top: 2px; }
</style>
</head>
<body>
<main class="flyer">
  <div class="scene scene-park" role="img" aria-label="Photo of the Hollins Park community garden sign among trees and grass"></div>
  <div class="scene scene-families" role="img" aria-label="Photo of families and children walking on a park path"></div>
  <div class="scene scene-runners" role="img" aria-label="Photo of runners and walkers on a road lined with autumn trees"></div>
  <div class="scene scene-faded" role="img" aria-label="Faded photo of runners in motion"></div>
  <div class="scene scene-faded-lower"></div>

  <svg class="ribbons" width="1200" height="900" viewBox="0 0 1200 900" aria-hidden="true">
    <path d="M0 150 C120 190 220 250 330 268 C430 282 520 250 620 252 C780 256 980 370 1200 470" fill="none" stroke="var(--ribbon-red)" stroke-width="14"/>
    <path d="M0 166 C120 206 220 264 330 282 C430 296 520 264 620 266 C780 270 980 384 1200 484" fill="none" stroke="var(--ribbon-blue)" stroke-width="14"/>
    <path d="M0 182 C120 222 220 278 330 296 C430 310 520 278 620 280 C780 284 980 398 1200 498" fill="none" stroke="var(--ribbon-yellow)" stroke-width="14"/>
  </svg>

  <div class="footprints" role="img" aria-label="Illustration of white footprints"></div>

  <div class="logo-badge">
    <span class="logo-name">BEXOR</span>
  </div>

  <h1 class="title">
    <span class="title-main">5K WALK</span>
    <span class="title-sub">FOR AWARENESS</span>
    <span class="title-sub">AND STIGMA REMOVAL</span>
  </h1>

  <p class="extras">moon bounce, refreshments, and information!</p>

  <p class="event-details">
    <span class="event-date">MAY 18, 2014</span>
    <span class="event-time">10 am</span>
    <span class="event-place">Hollins Park</span>
    <span class="event-place">Medford N.J</span>
  </p>

  <div class="signup-panel"></div>
  <p class="signup-text">
    <span class="signup-heading">SIGN UP AS A VIRTUAL WALKER!</span>
    <span class="signup-link">http://www.bexor.org/training-events/<br>ADHD-walk-family-fun-day/virtual-walk.aspx</span>
    <span class="signup-or">or</span>
    <span class="signup-email">E-mail dianemercer22@example.com</span>
    <span class="signup-confirm">and CONFIRM AS AN EVENT WALKER</span>
  </p>
</main>
</body>
</html>
```